Design logo and business card.

Design and construct logo and card for my business which is an over seeing company of other smaller businesses. The companies name is eleven5 venture alliance. Im open to any ideas but i am looking for a very cool contemporary design with a very prestige feel. The card can be either single or double sided, Thank you and i will look forward to your submissions.

Industry/Entity Type

Business

Requirements
Must have
• Company name, email, website, telephone, my name. Cool modern look with a prestige feel.

```html
<!DOCTYPE html>
<html lang="en">
<head>
<meta charset="utf-8">
<title>eleven5 venture alliance — business card options</title>
<link rel="stylesheet" href="https://fonts.googleapis.com/css2?family=Open+Sans:wght@400;600&family=Arimo:wght@700&display=swap">
<style>
  :root {
    --page: #ffffff;
    --ink: #222222;
    --card-dark: #262523;
    --pattern-light: #2e2d2b;
    --pattern-dark: #1c1b1a;
    --white: #ffffff;
    --gold: #f2c500;
    --gold-pale: #fff4c4;
  }
  * { margin: 0; padding: 0; box-sizing: border-box; }
  html, body { width: 1200px; height: 1000px; overflow: hidden; background: var(--page); }
  .sheet { position: relative; width: 1200px; height: 1000px; font-family: "Open Sans", Arial, sans-serif; }

  .option-number {
    position: absolute;
    font-family: "Arimo", Arial, sans-serif;
    font-weight: 700;
    font-size: 58px;
    line-height: 1;
    color: var(--ink);
  }

  .card {
    position: absolute;
    width: 373px;
    height: 215px;
    border-radius: 15px;
    overflow: hidden;
    background: var(--card-dark);
    color: var(--white);
  }
  .card-pattern {
    position: absolute;
    left: 0; top: 0; width: 100%; height: 100%;
    background: radial-gradient(ellipse at 50% 40%, var(--pattern-light), var(--pattern-dark));
  }

  /* front */
  .brand-name {
    position: absolute;
    left: 0; right: 0; top: 88px;
    text-align: center;
    font-size: 25px;
    font-weight: 400;
    letter-spacing: 0.3px;
    color: var(--white);
  }
  .card--gold .brand-name { color: var(--gold); }
  .front-band { position: absolute; left: 0; top: 180px; width: 373px; height: 16px; }
  .web-address {
    position: absolute;
    left: 227px; top: 180px;
    font-size: 10.5px;
    line-height: 16px;
    color: var(--white);
  }

  /* back */
  .back-head {
    position: absolute;
    left: 0; top: 0; width: 100%; height: 113px;
  }
  .back-title {
    position: absolute;
    left: 0; right: 0; top: 74px;
    text-align: center;
    font-size: 18.5px;
    font-weight: 400;
    letter-spacing: 0.2px;
  }
  .back-rule { position: absolute; left: 0; top: 113px; width: 100%; height: 5px; background: var(--white); }
  .card--gold .back-rule { background: linear-gradient(90deg, var(--gold-pale), var(--gold) 30%, var(--gold) 75%, var(--gold-pale)); }
  .contact { position: absolute; left: 0; right: 0; top: 134px; text-align: center; }
  .contact-name { font-size: 15px; line-height: 20px; }
  .contact-line { font-size: 10px; font-weight: 600; line-height: 17px; display: flex; justify-content: center; align-items: center; gap: 3px; }
  .contact-line svg { width: 8px; height: 8px; }
</style>
</head>
<body>
<main class="sheet">
  <span class="option-number" style="left:88px;top:88px;">1</span>
  <span class="option-number" style="left:1076px;top:76px;">2</span>
  <span class="option-number" style="left:58px;top:733px;">3</span>
  <span class="option-number" style="left:1077px;top:713px;">4</span>

  <!-- option 1 -->
  <section class="card card--front" style="left:218px;top:2px;">
    <div class="card-pattern" role="img" aria-label="Dark grey damask wallpaper pattern"></div>
    <div class="brand-name">eleven5 venture alliance</div>
    <svg class="front-band" viewBox="0 0 373 16"><rect x="0" y="4" width="220" height="7" fill="#ffffff"/><polygon points="339,4 373,4 373,11 337,11" fill="#ffffff"/></svg>
    <div class="web-address">www. eleven-5.com</div>
  </section>
  <section class="card card--back" style="left:215px;top:255px;">
    <div class="back-head card-pattern" role="img" aria-label="Dark grey damask wallpaper pattern"></div>
    <div class="back-title">ELEVEN5 VENTURE ALLIANCE</div>
    <div class="back-rule"></div>
    <div class="contact">
      <div class="contact-name">KAI MOREN</div>
      <div class="contact-line"><svg viewBox="0 0 8 8"><rect x="2" y="0.5" width="4" height="7" rx="0.8" fill="none" stroke="#fff" stroke-width="0.9"/></svg>+34 611 204 587</div>
      <div class="contact-line"><svg viewBox="0 0 8 8"><rect x="0.5" y="1.5" width="7" height="5" fill="none" stroke="#fff" stroke-width="0.9"/><polyline points="0.5,1.5 4,4.5 7.5,1.5" fill="none" stroke="#fff" stroke-width="0.9"/></svg>info@eleven-5.com</div>
    </div>
  </section>

  <!-- option 2 -->
  <section class="card card--front" style="left:625px;top:2px;">
    <div class="card-pattern" role="img" aria-label="Dark grey damask wallpaper pattern"></div>
    <div class="brand-name">eleven5 venture alliance</div>
    <svg class="front-band" viewBox="0 0 373 16"><rect x="0" y="4" width="220" height="7" fill="#ffffff"/><polygon points="337,4 373,4 373,11 335,11" fill="#ffffff"/></svg>
    <div class="web-address">www. eleven-5.com</div>
  </section>
  <section class="card card--back" style="left:622px;top:255px;">
    <div class="back-head card-pattern" role="img" aria-label="Dark grey damask wallpaper pattern"></div>
    <div class="back-title">ELEVEN5 VENTURE ALLIANCE</div>
    <div class="back-rule"></div>
    <div class="contact">
      <div class="contact-name">KAI MOREN</div>
      <div class="contact-line"><svg viewBox="0 0 8 8"><rect x="2" y="0.5" width="4" height="7" rx="0.8" fill="none" stroke="#fff" stroke-width="0.9"/></svg>+34 611 204 587</div>
      <div class="contact-line"><svg viewBox="0 0 8 8"><rect x="0.5" y="1.5" width="7" height="5" fill="none" stroke="#fff" stroke-width="0.9"/><polyline points="0.5,1.5 4,4.5 7.5,1.5" fill="none" stroke="#fff" stroke-width="0.9"/></svg>info@eleven-5.com</div>
    </div>
  </section>

  <!-- option 3 -->
  <section class="card card--front card--gold" style="left:208px;top:528px;">
    <div class="card-pattern" role="img" aria-label="Dark grey damask wallpaper pattern"></div>
    <div class="brand-name">eleven5 venture alliance</div>
    <svg class="front-band" viewBox="0 0 373 16">
      <defs><linearGradient id="goldBandA" x1="0" x2="1"><stop offset="0" stop-color="#fff4c4"/><stop offset="0.35" stop-color="#f2c500"/><stop offset="1" stop-color="#f2c500"/></linearGradient></defs>
      <rect x="0" y="4" width="220" height="7" fill="url(#goldBandA)"/><polygon points="339,4 373,4 373,11 337,11" fill="#f2c500"/>
    </svg>
    <div class="web-address">www. eleven-5.com</div>
  </section>
  <section class="card card--back card--gold" style="left:206px;top:781px;">
    <div class="back-head card-pattern" role="img" aria-label="Dark grey damask wallpaper pattern"></div>
    <div class="back-title">ELEVEN5 VENTURE ALLIANCE</div>
    <div class="back-rule"></div>
    <div class="contact">
      <div class="contact-name">KAI MOREN</div>
      <div class="contact-line"><svg viewBox="0 0 8 8"><rect x="2" y="0.5" width="4" height="7" rx="0.8" fill="none" stroke="#fff" stroke-width="0.9"/></svg>+34 611 204 587</div>
      <div class="contact-line"><svg viewBox="0 0 8 8"><rect x="0.5" y="1.5" width="7" height="5" fill="none" stroke="#fff" stroke-width="0.9"/><polyline points="0.5,1.5 4,4.5 7.5,1.5" fill="none" stroke="#fff" stroke-width="0.9"/></svg>info@eleven-5.com</div>
    </div>
  </section>

  <!-- option 4 -->
  <section class="card card--front card--gold" style="left:615px;top:528px;">
    <div class="card-pattern" role="img" aria-label="Dark grey damask wallpaper pattern"></div>
    <div class="brand-name">eleven5 venture alliance</div>
    <svg class="front-band" viewBox="0 0 373 16">
      <defs><linearGradient id="goldBandB" x1="0" x2="1"><stop offset="0" stop-color="#fff4c4"/><stop offset="0.3" stop-color="#f2c500"/><stop offset="1" stop-color="#f2c500"/></linearGradient>
      <linearGradient id="goldTipB" x1="0" x2="1"><stop offset="0" stop-color="#fff4c4"/><stop offset="1" stop-color="#f2c500"/></linearGradient></defs>
      <rect x="0" y="4" width="220" height="7" fill="url(#goldBandB)"/><polygon points="341,4 373,4 373,11 337,11" fill="url(#goldTipB)"/>
    </svg>
    <div class="web-address">www. eleven-5.com</div>
  </section>
  <section class="card card--back card--gold" style="left:613px;top:781px;">
    <div class="back-head card-pattern" role="img" aria-label="Dark grey damask wallpaper pattern"></div>
    <div class="back-title">ELEVEN5 VENTURE ALLIANCE</div>
    <div class="back-rule"></div>
    <div class="contact">
      <div class="contact-name">KAI MOREN</div>
      <div class="contact-line"><svg viewBox="0 0 8 8"><rect x="2" y="0.5" width="4" height="7" rx="0.8" fill="none" stroke="#fff" stroke-width="0.9"/></svg>+34 611 204 587</div>
      <div class="contact-line"><svg viewBox="0 0 8 8"><rect x="0.5" y="1.5" width="7" height="5" fill="none" stroke="#fff" stroke-width="0.9"/><polyline points="0.5,1.5 4,4.5 7.5,1.5" fill="none" stroke="#fff" stroke-width="0.9"/></svg>info@eleven-5.com</div>
    </div>
  </section>
</main>
</body>
</html>
```